Design professional, clean and neat beauty clinic

design an instagram style flyer similar style but have my own branding. Like they have their own. Must look different but also similar/better in professionalism. source file also needed.

Font styles to use
Sans Serif

```html
<!DOCTYPE html>
<html lang="en">
<head>
<meta charset="utf-8">
<title>Beauty Therapy – Aesthetics Training Flyer</title>
<link href="https://fonts.googleapis.com/css2?family=Raleway:ital,wght@0,300;0,400;0,500;1,300;1,400&family=Nunito:ital,wght@1,800;1,900&family=Yellowtail&display=swap" rel="stylesheet">
<style>
  :root {
    --white: #ffffff;
    --ink: #2f3033;
    --grey-text: #6d6e71;
    --grey-band: #cfd0d2;
    --badge-blue: #4267b2;
    --orange-light: #f7a93b;
    --orange-mid: #ef6b3a;
    --red: #e8383a;
    --yellow: #f9e13a;
    --photo-light: #f1e2d8;
    --photo-dark: #3b2b27;
  }
  * { margin: 0; padding: 0; box-sizing: border-box; }
  html, body { width: 1199px; height: 1200px; overflow: hidden; background: var(--white); }
  .flyer { position: relative; width: 1199px; height: 1200px; overflow: hidden; background: var(--white); }
  .flyer__shapes { position: absolute; inset: 0; width: 1199px; height: 1200px; }
  .text { position: absolute; white-space: nowrap; line-height: 1; }

  .brand-name {
    left: 845px; top: 112px;
    font-family: "Raleway", sans-serif; font-weight: 500;
    font-size: 62px; color: var(--ink); letter-spacing: 0.5px;
  }
  .intro {
    left: 948px; top: 304px; transform: translateX(-50%);
    font-family: "Raleway", sans-serif; font-weight: 400;
    font-size: 42px; color: var(--white);
  }
  .headline {
    position: absolute; right: 59px; width: 560px; text-align: right;
    font-family: "Yellowtail", "Brush Script MT", sans-serif;
    font-weight: 400; color: var(--white);
    font-size: 150px; line-height: 1; white-space: nowrap;
  }
  .headline--first { top: 420px; padding-right: 155px; }
  .headline--second { top: 572px; }
  .subline {
    left: 620px; top: 804px; width: 450px; text-align: right;
    font-family: "Nunito", sans-serif; font-style: italic; font-weight: 900;
    font-size: 36px; line-height: 50px; color: var(--white); white-space: normal;
  }
  .price {
    position: absolute; left: 305px; top: 912px; transform: translate(-50%, -50%);
    width: 236px; height: 236px; text-align: center; color: var(--white);
    font-family: "Nunito", sans-serif; font-style: italic; font-weight: 900;
  }
  .price__currency { position: absolute; left: 0; right: 0; top: 20px; font-size: 78px; line-height: 1; }
  .price__amount { position: absolute; left: 0; right: 0; top: 102px; font-size: 68px; line-height: 1; letter-spacing: 1px; }
  .price__note { position: absolute; left: 78px; top: 166px; font-size: 38px; font-weight: 800; line-height: 1; }

  .info-lead {
    left: 600px; top: 1054px; transform: translateX(-50%);
    font-family: "Raleway", sans-serif; font-style: italic; font-weight: 400;
    font-size: 36px; color: var(--grey-text);
  }
  .contact {
    left: 597px; top: 1102px; transform: translateX(-50%);
    font-family: "Nunito", sans-serif; font-style: italic; font-weight: 800;
    font-size: 40px; color: var(--grey-text);
  }
</style>
</head>
<body>
<main class="flyer">
  <svg class="flyer__shapes" viewBox="187 187 1555 1558" preserveAspectRatio="none">
    <defs>
      <linearGradient id="band-grey" x1="0" y1="0" x2="1" y2="0">
        <stop offset="0" stop-color="var(--grey-band)"/>
        <stop offset="0.6" stop-color="var(--white)"/>
      </linearGradient>
      <linearGradient id="photo-tone" x1="0" y1="0.2" x2="1" y2="0.8">
        <stop offset="0" stop-color="var(--photo-light)"/>
        <stop offset="0.45" stop-color="#e6cbbd"/>
        <stop offset="1" stop-color="var(--photo-dark)"/>
      </linearGradient>
      <linearGradient id="swoosh-yellow" x1="0" y1="0" x2="0" y2="1">
        <stop offset="0" stop-color="#f8b733"/>
        <stop offset="1" stop-color="var(--yellow)"/>
      </linearGradient>
      <linearGradient id="swoosh-orange" x1="0" y1="0" x2="1" y2="0">
        <stop offset="0" stop-color="var(--orange-mid)"/>
        <stop offset="1" stop-color="#f39a3a"/>
      </linearGradient>
      <linearGradient id="circle-fill" x1="0.15" y1="0.1" x2="0.85" y2="0.8">
        <stop offset="0" stop-color="var(--orange-light)"/>
        <stop offset="0.5" stop-color="var(--orange-mid)"/>
        <stop offset="1" stop-color="var(--red)"/>
      </linearGradient>
      <linearGradient id="rule-fade" x1="0" y1="0" x2="1" y2="0">
        <stop offset="0" stop-color="#ffffff" stop-opacity="0"/>
        <stop offset="1" stop-color="#ffffff" stop-opacity="1"/>
      </linearGradient>
    </defs>

    <rect class="band" x="187" y="1430" width="1555" height="315" fill="url(#band-grey)"/>

    <path class="swoosh swoosh--yellow" d="M960,187 H1030 C1110,300 1165,430 1175,545 L1160,560 C1140,420 1080,300 960,187 Z" fill="url(#swoosh-yellow)"/>
    <path class="swoosh swoosh--orange" d="M187,1392 C330,1420 440,1428 485,1440 L470,1474 C380,1480 280,1478 187,1468 Z" fill="url(#swoosh-orange)"/>

    <path class="photo" role="img" aria-label="Photo: woman in profile receiving an aesthetic injection from gloved hands"
      d="M187,187 H960 C1080,300 1150,430 1165,600 L1000,1000 L942,1250 C800,1370 520,1412 187,1392 Z"
      fill="url(#photo-tone)"/>

    <circle class="feature-circle" cx="1400" cy="993" r="513" fill="url(#circle-fill)"/>
    <rect class="rule" x="1045" y="684" width="693" height="6" fill="url(#rule-fade)"/>
    <rect class="rule" x="1045" y="1165" width="693" height="6" fill="url(#rule-fade)"/>

    <circle class="price-badge" cx="582" cy="1370" r="153" fill="var(--badge-blue)"/>
  </svg>

  <div class="text brand-name">Logo Here</div>
  <div class="text intro">Introducing</div>
  <div class="headline headline--first">Beauty</div>
  <div class="headline headline--second">Therapy</div>
  <div class="text subline">Route to Aesthetics<br>Training courses</div>

  <div class="price">
    <span class="price__currency">$</span>
    <span class="price__amount">00.00</span>
    <span class="price__note">only</span>
  </div>

  <div class="text info-lead">For Further information</div>
  <div class="text contact">call: 1234567890 | email: youremail@mailbox.com</div>
</main>
</body>
</html>
```